Saveurs Du Matin

looking fo an e-commerce site something that will stand out the site domain will be saveursdumatin.example need somthing bold and refind as well; eye appealing and not too cartonish please visit our competetors to see waht we are going for they are (zestlyne.example, brantaro4u.example and quellabrookfarms.example) this site should have multiple pages mainly looking for a layout to start the site and code.

PLEASE REMEMBER WE REQUIRE THE CODE....

Target Market(s)

anyone who loves food or is fasinated by it

Industry/Entity Type

E-Commerce

Requirements
Must have
• .an easy to work site that makes sense and that is not all over the place it should have in the navigation feature: Olive oils, Balsamic Vinegars, Misc. Vinegars and oils, Specialty salts, organic spices, Specialty Spices, Kitchen Tools. also pleas use our logo in the design i have attached below
Nice to have
• clean and some spices, salt, pepermills, morter and pistels, olive oils, trying to stick to a clean presentation
Should not have
• no cartoon figures or alike, anything too playfull

```html
<!DOCTYPE html>
<html lang="en">
<head>
<meta charset="utf-8">
<title>Saveurs Du Matin — Highest Quality Spices</title>
<link href="https://fonts.googleapis.com/css2?family=Ubuntu:wght@400;500&family=PT+Sans+Narrow&family=Dancing+Script:wght@500&display=swap" rel="stylesheet">
<style>
:root{
  --brown:#6b2a12;
  --brown-text:#7a3210;
  --ink:#3b3b3b;
  --muted:#666;
  --topbar:#e8ddd6;
  --beige:#eddcd0;
  --section:#e6e4e2;
  --panel:#f4f4f4;
  --footer:#e5d7cd;
  --rule:#b9b1ab;
  --bullet:#e49b62;
}
*{margin:0;padding:0;box-sizing:border-box}
html,body{width:1200px;height:1172px;overflow:hidden}
body{position:relative;font-family:"Ubuntu",sans-serif;color:var(--ink);background:#fff}
a{color:inherit;text-decoration:none}
.abs{position:absolute}

.topbar{left:0;top:0;width:1200px;height:39px;background:var(--topbar)}
.account-links{right:152px;top:13px;font-size:10px;color:#555;word-spacing:2px}
.header-band{left:0;top:39px;width:1200px;height:111px;
  background:linear-gradient(#fff 0%,#faf5f2 50%,var(--beige) 100%);
  border-bottom:1px solid #d8c6b9;box-shadow:0 2px 3px rgba(0,0,0,.12)}
.header-band::after{content:"";position:absolute;left:0;right:0;top:61px;border-top:1px dashed #cdbdb1}

.logo-tab{left:150px;top:0;width:158px;height:200px}
.logo-name{left:150px;top:108px;width:158px;text-align:center;font-size:16px;color:var(--brown-text)}
.logo-mark{left:208px;top:28px;width:42px;height:42px;border-radius:50%;border:2px solid var(--bullet)}
.logo-tag{left:150px;top:146px;width:158px;text-align:center;font-family:"Dancing Script",cursive;font-size:10px;letter-spacing:2px;color:#444}

.phone{left:340px;top:58px;display:flex;align-items:center;gap:12px;color:var(--brown-text);font-size:15px}
.search{left:822px;top:57px;width:228px;height:27px;background:#f0ebe8;border:1px solid #cfc6c0;border-top-color:#bdb3ac}
.search span{position:absolute;left:13px;top:7px;font-size:11px;color:#666}
.search svg{position:absolute;right:7px;top:5px}

.main-nav{left:340px;top:117px;width:711px;display:flex;justify-content:space-between;font-family:"PT Sans Narrow",sans-serif;font-size:14px;color:var(--brown-text)}

.hero-arrow{top:288px}
.hero-title{left:240px;top:258px;width:350px;text-align:center;font-family:"Dancing Script",cursive;font-size:50px;color:var(--brown-text);line-height:1}
.hero-tag{left:290px;top:324px;font-family:"Dancing Script",cursive;font-size:17px;letter-spacing:4px;color:#333}
.hero-copy{left:252px;top:362px;width:342px;text-align:center;font-size:10.5px;line-height:17px;color:#666}
.hero-photo{left:600px;top:190px;width:370px;height:276px;border-radius:6px;
  background:radial-gradient(ellipse at 50% 40%,#e9c84a 0%,#d4aa2a 35%,#9aa746 62%,#fff 80%)}

.section{left:0;top:487px;width:1200px;height:516px;background:var(--section)}
.promo{top:500px;width:291px;height:138px;background:#fff;padding:5px;box-shadow:0 6px 6px -4px rgba(0,0,0,.35)}
.promo-inner{position:relative;width:100%;height:100%;background:linear-gradient(90deg,#dedcda,#c9c6c3)}
.promo-photo{position:absolute;right:0;top:0;width:120px;height:128px}
.promo h3{position:absolute;left:19px;top:16px;font-size:15px;font-weight:500;color:#4a2410}
.promo p{position:absolute;left:19px;top:48px;width:160px;font-size:10px;line-height:17px;color:#666;text-align:justify}
.promo .btn{position:absolute;right:2px;top:86px;width:110px;height:28px;background:var(--brown);color:#fff;font-size:13px;text-align:center;line-height:28px}

.rule{left:150px;width:895px;border-top:1px dashed var(--rule)}
.col-head{top:678px;font-size:15px;color:var(--brown-text)}

.panel{background:var(--panel);box-shadow:0 1px 2px rgba(0,0,0,.15)}
.cat-list{list-style:none;padding:10px 0 0 14px}
.cat-list li{font-size:11.5px;height:28px;line-height:28px;color:#333}
.cat-list li::before{content:"";display:inline-block;width:4px;height:4px;border-radius:50%;background:var(--bullet);margin-right:12px;vertical-align:middle}

.about-photo{left:393px;top:734px;width:225px;height:150px;background:linear-gradient(90deg,#6f7c7a,#d8ddd8 40%,#d4b32e 55%,#e8e6de 75%,#b5bbb7)}
.about-title{left:641px;top:734px;font-size:12px;color:#222}
.about-copy{left:641px;width:397px;font-size:9.5px;line-height:17px;color:#444;text-align:justify}
.about-foot{left:393px;top:900px;width:645px;font-size:9.5px;line-height:17px;color:#444}

.footer{left:0;top:1003px;width:1200px;height:169px;background:var(--footer);border-top:1px solid #cdb9aa}
.foot-brand{left:150px;top:1023px;display:flex;align-items:center;gap:8px;font-size:12px;color:#8a7a70}
.foot-brand i{width:18px;height:18px;border-radius:50%;border:1.5px solid #a59a92;display:block}
.copyright{left:150px;top:1113px;font-size:10.5px;color:#333}
.foot-head{font-size:15px;color:#333}
.socials{left:435px;top:1056px;display:flex;gap:9px}
.socials span{width:26px;height:26px;border-radius:50%;background:#9a9490;display:block}
.legal{left:379px;top:1111px;font-size:10.5px;color:#333;word-spacing:2px}
.quick{left:607px;top:1053px;list-style:none;font-size:11px;color:#333}
.quick li{height:22.5px}
.newsletter{left:836px;top:1025px;width:214px;height:131px;background:#e3d6cc;border:2px solid #d5c6bb;border-radius:3px;padding:13px 16px}
.newsletter h4{font-weight:400;font-size:15px;color:var(--brown-text)}
.newsletter p{margin-top:8px;font-size:10px;line-height:17px;color:#444}
.sub{margin-top:10px;display:flex;height:24px}
.sub .field{flex:1;background:#fff;border:1px solid #c9bdb4}
.sub .go{width:75px;background:var(--brown);color:#fff;font-size:11px;text-align:center;line-height:24px}
</style>
</head>
<body>

<div class="abs topbar"></div>
<nav class="abs account-links">My Account &nbsp;|&nbsp; Order Tracking &nbsp;|&nbsp; Wish List &nbsp;|&nbsp; View Cart &nbsp;/&nbsp; Checkout</nav>
<header class="abs header-band"></header>

<svg class="abs logo-tab" viewBox="0 0 158 200" aria-hidden="true">
  <defs><linearGradient id="tabfill" x1="0" y1="0" x2="0" y2="1"><stop offset="0" stop-color="#fff"/><stop offset="1" stop-color="#f1efee"/></linearGradient></defs>
  <path d="M0 0H158V182L79 200L0 182Z" fill="url(#tabfill)" stroke="#e2dcd8"/>
</svg>
<div class="abs logo-mark"></div>
<div class="abs logo-name">Saveurs Du Matin</div>
<div class="abs logo-tag">Highest Quality Spices</div>

<div class="abs phone">
  <svg width="27" height="27" viewBox="0 0 27 27" aria-hidden="true"><circle cx="13.5" cy="13.5" r="12" fill="none" stroke="#8a3a18" stroke-width="2"/><path d="M9 10c1-2 3-2 3-1l1 2-1 1c0 2 2 4 4 4l1-1 2 1c1 0 1 2-1 3-4 1-10-5-9-9z" fill="#8a3a18"/></svg>
  <span>Call : 1-800-555-0147</span>
</div>
<div class="abs search"><span>Search</span>
  <svg width="16" height="16" viewBox="0 0 16 16" aria-hidden="true"><circle cx="6.5" cy="6.5" r="4.5" fill="none" stroke="#7a3210" stroke-width="2"/><path d="M10 10l4.5 4.5" stroke="#7a3210" stroke-width="2.5"/></svg>
</div>

<nav class="abs main-nav">
  <a>Olive oils</a><a>Balsamic Vinegars</a><a>Misc</a><a>Vinegars and oils</a><a>Specialty salts</a><a>Organic spices</a><a>Specialty Spices</a><a>Kitchen Tools</a>
</nav>

<svg class="abs hero-arrow" style="left:150px" width="36" height="60" viewBox="0 0 36 60" aria-hidden="true"><path d="M36 0H22L0 30L22 60H36L14 30Z" fill="#d6d6d6"/></svg>
<svg class="abs hero-arrow" style="left:1011px" width="36" height="60" viewBox="0 0 36 60" aria-hidden="true"><path d="M0 0H14L36 30L14 60H0L22 30Z" fill="#d6d6d6"/></svg>
<div class="abs hero-title">Saveurs Du Matin</div>
<div class="abs hero-tag">Highest Quality Spices</div>
<p class="abs hero-copy">Lorem Ipsum is simply dummy text of the printing and typesetting industry. Lorem Ipsum has been the industry's standard dummy text ever since the 1500s, when an unknown printer .</p>
<div class="abs hero-photo" role="img" aria-label="Four corked bottles of olive oil with green and black olives and olive leaves"></div>

<div class="abs section"></div>

<article class="abs promo" style="left:150px"><div class="promo-inner">
  <div class="promo-photo" role="img" aria-label="Bottle and small dish of olive oil" style="background:linear-gradient(90deg,transparent,#c9b24a 45%,#a88a1c 60%,transparent)"></div>
  <h3>Olive Oils</h3><p>For Italian extra virgin olive oil, Brantaro4u is the leading source on the Internet.</p><a class="btn">View all</a>
</div></article>
<article class="abs promo" style="left:457px"><div class="promo-inner" style="background:linear-gradient(90deg,#cfcdca,#b8b5b1)">
  <div class="promo-photo" role="img" aria-label="Jar and plate of mixed peppercorns" style="background:linear-gradient(90deg,transparent,#8a6a5a 45%,#6d4b3a 65%,transparent)"></div>
  <h3>Organic Spices</h3><p>For Italian extra virgin olive oil, Brantaro4u is the leading source on the Internet.</p><a class="btn">View all</a>
</div></article>
<article class="abs promo" style="left:761px"><div class="promo-inner" style="background:linear-gradient(90deg,#efefef,#dcdcdc)">
  <div class="promo-photo" role="img" aria-label="Wall rack with hanging kitchen utensils and spice tubes" style="width:165px;background:linear-gradient(90deg,transparent,#d0d0d0 30%,#5a5a5a 60%,#c8c8c8 85%,transparent)"></div>
  <h3>Kitchen Tools</h3><a class="btn">View all</a>
</div></article>

<div class="abs rule" style="top:671px"></div>
<div class="abs rule" style="top:705px"></div>
<h2 class="abs col-head" style="left:164px;font-weight:400">Categories</h2>
<h2 class="abs col-head" style="left:393px;font-weight:400">About Us</h2>

<aside class="abs panel" style="left:150px;top:717px;width:215px;height:254px">
  <ul class="cat-list">
    <li>Olive oils</li><li>Balsamic Vinegars</li><li>Misc</li><li>Vinegars and oils</li><li>Pecialty salts</li><li>Organic spices</li><li>Specialty Spices</li><li>Kitchen Tools</li>
  </ul>
</aside>
<section class="abs panel" style="left:379px;top:717px;width:671px;height:254px"></section>
<div class="abs about-photo" role="img" aria-label="Glass and bottle of golden olive oil"></div>
<h3 class="abs about-title" style="font-weight:400">Featuring Unfiltered Extra Virgin Olive Oils and Aged Balsamic Vinegars</h3>
<p class="abs about-copy" style="top:768px">With its roots firmly planted in tradition, saveurs du matin Olive Oils &amp; Vinegars is forging a new image of the modern artisan.</p>
<p class="abs about-copy" style="top:818px">From a true respect for the olive tree to the insistence on quality and authenticity, Saveurs's extra virgin unfiltered olive oil (EVOO) offers transparency and purity for the consumer who respects the harmony of nature and nutrition.</p>
<p class="abs about-foot">Saveurs features in-store tasting rooms offering a wide selection of premium extra virgin, first, cold pressed olive oil from around the world and aged balsamic vinegar from Modena, Italy.</p>

<footer class="abs footer"></footer>
<div class="abs foot-brand"><i></i>Saveurs Du Matin</div>
<div class="abs copyright">Copyright © 2012. All Rights Reserved</div>
<h4 class="abs foot-head" style="left:379px;top:1027px;font-weight:400">Social Media</h4>
<div class="abs socials"><span></span><span></span><span></span></div>
<div class="abs legal">Terms &amp; Condition &nbsp;&nbsp;|&nbsp;&nbsp; Privacy Policy</div>
<h4 class="abs foot-head" style="left:607px;top:1022px;font-weight:400">Quick Links:</h4>
<ul class="abs quick" style="top:1056px"><li>Recipes</li><li>Restaurants</li><li>History of Olive Oil</li><li>About saveurs</li></ul>
<div class="abs newsletter">
  <h4>Newsletter</h4>
  <p>Enter your email address to join our mailing list</p>
  <div class="sub"><span class="field"></span><span class="go">Sign Up</span></div>
</div>

</body>
</html>
```